Professional looking Roller Blind Discount Card that portrays quality at a value for money price!

We need a double sided business card designed as a discount card. Size 90mm wide x 55mm high.We would like it to look professional and portray quality at a value for money price point.I have uploaded a word document with a basic layout with the information we want included on each side of the card. Please put your own thought into the layout.

Contact Information for Business Card

As per word document attached.

```html
<!DOCTYPE html>
<html lang="en">
<head>
<meta charset="utf-8">
<title>Roller Blinds Discount Card</title>
<link href="https://fonts.googleapis.com/css2?family=Oswald:wght@500;700&family=Orbitron:wght@900&family=Tinos&display=swap" rel="stylesheet">
<style>
  :root{
    --page:#111;
    --card:#1f1f1f;
    --card-dark:#161616;
    --orange:#e8901c;
    --gold-light:#f6d46a;
    --gold:#d9a62c;
    --gold-dark:#9c6d14;
    --brown:#6a3a12;
    --blue:#1a8fd8;
    --blue-deep:#1f5fb4;
    --white:#ffffff;
  }
  *{margin:0;padding:0;box-sizing:border-box}
  html,body{width:1200px;height:1200px;overflow:hidden;background:var(--page)}
  .canvas{position:relative;width:1200px;height:1200px}
  .card{position:absolute;width:725px;height:443px;background:var(--card);overflow:hidden;box-shadow:0 10px 30px rgba(0,0,0,.7)}
  .card--front{left:183px;top:165px}
  .card--back{left:366px;top:674px}

  .offer-box{position:absolute;left:56px;top:0;width:221px;height:163px;border:4px solid var(--orange);border-top:none;background:#262626}
  .offer-num{position:absolute;left:12px;top:14px;font:900 88px/1 'Orbitron',sans-serif;color:var(--white);letter-spacing:-2px}
  .offer-pct{position:absolute;left:168px;top:24px;font:900 36px/1 'Orbitron',sans-serif;color:var(--white)}
  .offer-off{position:absolute;left:30px;top:106px;font:900 44px/1 'Orbitron',sans-serif;color:var(--white)}
  .headline{position:absolute;left:290px;top:66px;font:700 25px/31px 'Oswald',sans-serif;color:var(--white)}

  .medal{position:absolute;width:176px;height:176px;border-radius:50%;top:190px;
    background:radial-gradient(circle at 35% 30%,var(--gold-light),var(--gold) 55%,var(--gold-dark));
    box-shadow:4px 8px 14px rgba(0,0,0,.6);display:flex;align-items:center;justify-content:center}
  .medal::before{content:"";position:absolute;inset:24px;border-radius:50%;border:1.5px solid var(--gold-dark)}
  .medal span{position:relative;font:700 14px/19px 'Oswald',sans-serif;color:var(--brown);text-align:center;text-transform:uppercase}
  .medal--1{left:81px}.medal--2{left:274px}.medal--3{left:469px}

  .call-bar{position:absolute;left:33px;top:398px;width:659px;height:44px;border:3px solid var(--orange);border-top:none;
    display:flex;align-items:center;justify-content:center;gap:12px;font:900 29px/1 'Orbitron',sans-serif;color:var(--white)}
  .call-bar::before,.call-bar::after{content:"";position:absolute;top:0;width:20px;height:3px;background:var(--orange)}
  .call-bar::before{left:0}.call-bar::after{right:0}
  .call-bar .call{color:var(--blue)}

  .brand{position:absolute;left:60px;top:96px;width:220px;display:flex;align-items:center;gap:8px;justify-content:center}
  .brand-mark{width:14px;height:14px;background:var(--blue-deep)}
  .brand-name{font:400 26px/1 'Tinos',serif;color:var(--blue-deep)}
  .title{position:absolute;left:307px;top:36px;font:700 60px/1 'Oswald',sans-serif;color:var(--blue);letter-spacing:-1px}
  .subtitle{position:absolute;left:307px;top:108px;font:700 25px/1 'Oswald',sans-serif;color:var(--white)}
  .photo-area{position:absolute;left:0;top:0}
  .fabric-badge{position:absolute;left:56px;top:258px;width:104px;height:104px;border-radius:50%;background:var(--white);
    display:flex;align-items:center;justify-content:center;text-align:center;font:700 15px/19px 'Oswald',sans-serif;color:#111}
</style>
</head>
<body>
<div class="canvas">
  <section class="card card--front">
    <div class="offer-box">
      <div class="offer-num">25</div>
      <div class="offer-pct">%</div>
      <div class="offer-off">OFF</div>
    </div>
    <p class="headline">QUALITY CUSTOM MADE ROLLER BLINDS<br>BLOCKOUT – SCREEN – LIGHT FILTERING</p>
    <div class="medal medal--1"><span>Free in home<br>measure &amp; quote</span></div>
    <div class="medal medal--2"><span>Best price<br>guarantee</span></div>
    <div class="medal medal--3"><span>Family owned<br>&amp; operated</span></div>
    <div class="call-bar"><span class="call">CALL</span><span>0400 123 456 TODAY!</span></div>
  </section>

  <section class="card card--back">
    <svg class="photo-area" width="725" height="443" viewBox="0 0 725 443">
      <defs>
        <linearGradient id="photoTone" x1="0" x2="1" y1="0" y2="0">
          <stop offset="0" stop-color="#5a4438"/>
          <stop offset="0.25" stop-color="#3f5a32"/>
          <stop offset="0.7" stop-color="#5c7a4a"/>
          <stop offset="1" stop-color="#b0a59a"/>
        </linearGradient>
      </defs>
      <polygon points="0,234 725,136 725,166 0,254" fill="#101010"/>
      <polygon role="img" aria-label="Photo of a room with roller blinds over glass doors opening to a garden" points="0,254 725,166 725,376 0,376" fill="url(#photoTone)"/>
      <rect x="0" y="376" width="725" height="67" fill="#1a1a1a"/>
    </svg>
    <div class="brand"><span class="brand-mark"></span><span class="brand-name">Northway Blinds</span></div>
    <div class="title">ROLLER BLINDS</div>
    <div class="subtitle">FREE IN HOME MEASURE &amp; QUOTE</div>
    <div class="fabric-badge">HUGE<br>SELECTION OF<br>FABRICS</div>
    <div class="call-bar"><span class="call">CALL</span><span>0400 123 456 TODAY!</span></div>
  </section>
</div>
</body>
</html>
```